TALBRIN ELEVATOR CORP

LOOKING FOR BLACK MATTE BACKGROUND WITH GLOSS DESIGN
NEED RAISED UV ON LOGO AND LETTERING , WITH ROUNDED CORNERS AND COLORED EDGES ( FLOURECENT BLUE)

```html
<!DOCTYPE html>
<html lang="en">
<head>
<meta charset="utf-8">
<title>Talbrin Elevator Corp – Business Card</title>
<link href="https://fonts.googleapis.com/css2?family=Lato:wght@400;700;900&family=Libre+Baskerville&display=swap" rel="stylesheet">
<style>
  :root {
    --stage: #5b5b5b;
    --card-dark: #2d2b2c;
    --card-black: #252324;
    --paper: #ffffff;
    --brand-blue: #1f5bb8;
    --brand-teal: #2f7f9a;
    --brand-green: #3ba33a;
    --ink: #111111;
    --ink-soft: #3a3a3a;
    --silver: #b9b9b9;
    --contact: #f2f2f2;
  }
  * { margin: 0; padding: 0; box-sizing: border-box; }
  html, body { width: 1200px; height: 900px; overflow: hidden; }
  body {
    background: var(--stage);
    display: flex;
    align-items: center;
    justify-content: center;
    gap: 40px;
    font-family: "Lato", sans-serif;
  }
  .card {
    position: relative;
    width: 540px;
    height: 310px;
    border-radius: 16px;
    overflow: hidden;
  }
  .card-front { background: var(--paper); }
  .card-back { background: var(--card-black); }

  .front-wave { position: absolute; inset: 0; }

  .brand {
    position: absolute;
    left: 46px;
    top: 40px;
    display: flex;
    align-items: center;
    gap: 14px;
  }
  .brand-dot {
    width: 62px; height: 62px;
    border-radius: 50%;
    background: var(--brand-blue);
  }
  .brand-name {
    font-weight: 900;
    font-size: 17px;
    line-height: 1.02;
    color: var(--ink);
    letter-spacing: 0.5px;
  }

  .holder {
    position: absolute;
    right: 34px;
    top: 96px;
    text-align: right;
  }
  .holder-name {
    font-weight: 900;
    font-size: 30px;
    letter-spacing: 0.5px;
    line-height: 1;
  }
  .holder-name .first { color: var(--brand-blue); }
  .holder-name .last { color: var(--brand-green); }
  .holder-role, .holder-company {
    font-size: 15px;
    color: var(--ink-soft);
    line-height: 1.3;
  }
  .holder-role { margin-top: 4px; }

  .contact {
    position: absolute;
    right: 118px;
    top: 206px;
    list-style: none;
    text-align: right;
    color: var(--contact);
    font-size: 13.5px;
    line-height: 17px;
  }
  .contact li { display: flex; justify-content: flex-end; align-items: center; gap: 8px; }
  .contact .icon { width: 13px; height: 13px; flex: none; }
  .contact .no-icon { padding-right: 21px; }

  .back-mark {
    position: absolute;
    inset: 0;
    display: flex;
    flex-direction: column;
    align-items: center;
    justify-content: center;
  }
  .back-dot {
    width: 92px; height: 92px;
    border-radius: 50%;
    background: var(--brand-blue);
    margin-bottom: 12px;
  }
  .back-title {
    display: flex;
    align-items: center;
    gap: 14px;
    font-family: "Libre Baskerville", serif;
    color: var(--silver);
  }
  .back-title .rule {
    width: 60px; height: 2px;
    background: var(--silver);
  }
  .back-name { font-size: 20px; letter-spacing: 1px; }
  .back-tagline {
    font-family: "Libre Baskerville", serif;
    color: var(--silver);
    font-size: 13px;
    letter-spacing: 1px;
    margin-top: 4px;
  }
</style>
</head>
<body>

  <section class="card card-front">
    <svg class="front-wave" viewBox="0 0 540 310" aria-hidden="true">
      <defs>
        <linearGradient id="waveTone" x1="0" y1="0" x2="1" y2="0">
          <stop offset="0" stop-color="var(--brand-blue)"/>
          <stop offset="0.45" stop-color="var(--brand-teal)"/>
          <stop offset="1" stop-color="var(--brand-green)"/>
        </linearGradient>
      </defs>
      <path d="M0 34 C 60 30, 70 140, 200 150 C 330 160, 450 180, 520 310 L 0 310 Z" fill="url(#waveTone)"/>
      <path d="M0 46 C 62 44, 74 148, 200 158 C 330 168, 440 190, 500 310 L 0 310 Z" fill="var(--paper)"/>
      <path d="M0 56 C 66 56, 80 156, 200 166 C 325 176, 430 198, 485 310 L 0 310 Z" fill="var(--card-dark)"/>
    </svg>

    <div class="brand">
      <span class="brand-dot"></span>
      <span class="brand-name">TALBRIN<br>ELEVATOR<br>CORP</span>
    </div>

    <div class="holder">
      <h1 class="holder-name"><span class="first">DORIAN</span> <span class="last">WELSH</span></h1>
      <p class="holder-role">President</p>
      <p class="holder-company">Talbrin Elevator Corp</p>
    </div>

    <ul class="contact">
      <li class="no-icon">2217 Harlow Street,</li>
      <li class="no-icon">Bronx, NY 10468</li>
      <li>516-555-0142
        <svg class="icon" viewBox="0 0 16 16" aria-hidden="true"><path d="M3 1h3l1.5 4-2 1.3a9 9 0 0 0 4.2 4.2L11 8.5l4 1.5v3a2 2 0 0 1-2 2A12 12 0 0 1 1 3a2 2 0 0 1 2-2z" fill="var(--contact)"/></svg>
      </li>
      <li>talbrinelevator@mail.com
        <svg class="icon" viewBox="0 0 16 16" aria-hidden="true"><rect x="1" y="3" width="14" height="10" fill="var(--contact)"/><path d="M1 3l7 6 7-6" stroke="var(--card-dark)" stroke-width="1.4" fill="none"/></svg>
      </li>
      <li>www.talbrinelevatorny.com
        <svg class="icon" viewBox="0 0 16 16" aria-hidden="true"><circle cx="8" cy="8" r="7" fill="none" stroke="var(--contact)" stroke-width="1.4"/><path d="M1 8h14M8 1c3 3 3 11 0 14M8 1c-3 3-3 11 0 14" stroke="var(--contact)" stroke-width="1.1" fill="none"/></svg>
      </li>
    </ul>
  </section>

  <section class="card card-back">
    <div class="back-mark">
      <span class="back-dot"></span>
      <div class="back-title">
        <span class="rule"></span>
        <span class="back-name">TALBRIN ELEVATOR CORP</span>
        <span class="rule"></span>
      </div>
      <p class="back-tagline">ELEVATOR SERVICES</p>
    </div>
  </section>

</body>
</html>
```